Nestlyo Business Card Project showing the logo and a vonka image on the rear

Design a whacky but professional business card, the logo is for the front and the Vonka image is for the rear. Happy to consider other open source Vonka Images if the designer wants to select one from the web. Nestlyo is a competitor to KPX.com.au and Plotfield.com.au and is based around every property in Australia

Business

Name, Title, Email, Web, Phone Number

• avenir

• Image on Back logo on front
• Happy to consider other images on rear, preftably Oscar Vonka. Image supplied I own, we can use open source other Vonka Images

```html
<!DOCTYPE html>
<html lang="en">
<head>
<meta charset="utf-8">
<title>Nestlyo Business Cards</title>
<link rel="stylesheet" href="https://fonts.googleapis.com/css2?family=Nunito+Sans:wght@400;800&display=swap">
<style>
  :root {
    --orange: #e88a27;
    --ink: #111111;
    --paper: #ffffff;
    --backdrop: #2a2a2e;
    --night: #1d4fa3;
    --sky: #5cc6e0;
    --magenta: #d8268c;
    --red: #e0383a;
    --yellow: #f2d21b;
    --green: #5fb342;
    --purple: #7a3fa0;
    --muted: #2b2b2b;
  }
  * { box-sizing: border-box; margin: 0; padding: 0; }
  html, body { width: 1200px; height: 800px; overflow: hidden; }
  body {
    background: var(--backdrop);
    font-family: "Nunito Sans", "Avenir", sans-serif;
    display: flex;
    align-items: center;
    justify-content: center;
    gap: 40px;
  }
  .card {
    position: relative;
    width: 540px;
    height: 310px;
    overflow: hidden;
    border-radius: 2px;
    box-shadow: 0 12px 30px rgba(0,0,0,0.45);
  }
  .brand {
    display: flex;
    align-items: center;
    gap: 12px;
  }
  .brand__dot { flex: none; }
  .brand__name {
    font-weight: 800;
    color: var(--ink);
    letter-spacing: 0.5px;
    line-height: 1;
  }

  /* Rear card */
  .card--rear { background: var(--orange); }
  .card--rear .brand {
    position: absolute;
    top: 30px;
    left: 160px;
  }
  .card--rear .brand__dot { width: 24px; height: 24px; background: var(--paper); }
  .card--rear .brand__name { font-size: 42px; }
  .cityscape {
    position: absolute;
    left: 0;
    top: 98px;
    width: 100%;
    height: 150px;
    border-top: 2px solid var(--ink);
    border-bottom: 2px solid var(--ink);
    background:
      linear-gradient(90deg,
        var(--purple) 0%, var(--magenta) 18%, var(--yellow) 30%, var(--green) 40%,
        var(--magenta) 52%, var(--red) 64%, var(--yellow) 72%, var(--red) 82%,
        var(--green) 90%, var(--purple) 100%) bottom / 100% 62% no-repeat,
      linear-gradient(90deg, var(--sky) 0%, var(--sky) 45%, var(--night) 55%, var(--night) 100%);
  }
  .rear__url {
    position: absolute;
    top: 264px;
    right: 70px;
    font-size: 15px;
    color: var(--ink);
    letter-spacing: 0.5px;
  }
  .rear__url strong { font-weight: 800; }

  /* Front card */
  .card--front { background: var(--paper); }
  .card--front::after {
    content: "";
    position: absolute;
    left: 0; right: 0; bottom: 0;
    height: 6px;
    background: var(--orange);
  }
  .front__content {
    position: absolute;
    left: 110px;
    top: 66px;
  }
  .card--front .brand { gap: 14px; }
  .card--front .brand__dot { width: 26px; height: 26px; background: var(--orange); }
  .card--front .brand__name { font-size: 52px; }
  .person { margin-top: 14px; margin-left: 100px; }
  .person__name {
    font-size: 26px;
    font-weight: 800;
    color: var(--orange);
    line-height: 1.1;
  }
  .person__title {
    font-size: 14px;
    color: var(--muted);
    letter-spacing: 0.5px;
  }
  .contact {
    margin-top: 18px;
    margin-left: 100px;
    padding-left: 14px;
    border-left: 1px solid var(--ink);
    list-style: none;
  }
  .contact__item {
    display: flex;
    align-items: center;
    gap: 8px;
    font-size: 12px;
    color: var(--muted);
    line-height: 1.6;
    letter-spacing: 0.3px;
    white-space: nowrap;
  }
  .contact__icon { width: 11px; height: 11px; flex: none; }
</style>
</head>
<body>

  <section class="card card--rear" aria-label="Card reverse">
    <div class="brand">
      <span class="brand__dot"></span>
      <span class="brand__name">Nestlyo</span>
    </div>
    <div class="cityscape" role="img" aria-label="Colourful cartoon city skyline of bright buildings, daytime sky with a sun on the left turning into a starry night sky with a moon on the right"></div>
    <p class="rear__url">www.<strong>nestlyo</strong>.com.au</p>
  </section>

  <section class="card card--front" aria-label="Card front">
    <div class="front__content">
      <div class="brand">
        <span class="brand__dot"></span>
        <span class="brand__name">Nestlyo</span>
      </div>
      <div class="person">
        <p class="person__name">Elliot Marsh</p>
        <p class="person__title">Founder &amp; CEO</p>
      </div>
      <ul class="contact">
        <li class="contact__item">
          <svg class="contact__icon" viewBox="0 0 12 12"><path d="M2.5 1 L4.5 1 L5.2 3.5 L4 4.5 Q5 7 7.5 8 L8.5 6.8 L11 7.5 L11 9.5 Q10.5 11 9 11 Q1 10 1 2.5 Q1 1 2.5 1 Z" fill="var(--orange)"/></svg>
          +0 (00) 000 0000
        </li>
        <li class="contact__item">
          <svg class="contact__icon" viewBox="0 0 12 12"><rect x="0.5" y="2" width="11" height="8" fill="var(--orange)"/><path d="M0.5 2 L6 6.5 L11.5 2" fill="none" stroke="#fff" stroke-width="1"/></svg>
          e.marsh@yourdomain.com.au
        </li>
        <li class="contact__item">
          <svg class="contact__icon" viewBox="0 0 12 12"><g fill="none" stroke="var(--orange)" stroke-width="1"><circle cx="6" cy="6" r="5"/><ellipse cx="6" cy="6" rx="2.2" ry="5"/><line x1="1" y1="6" x2="11" y2="6"/></g></svg>
          www.yourdomain.com.au
        </li>
      </ul>
    </div>
  </section>

</body>
</html>
```